Trucking Company Website Design

We are working with a Trucking company in California. They provide trucking services for dirt, gravel, landscape bark, and landscape materials.

As you might imagine, there are no websites we could find for inspiration for trucking companies.

Thank you for taking the time to consider designing a website for us. We are web developers based in Stockton, CA, USA. Most of our projects go through the same process. Understanding this process may help you win a project with us. We custom-code all of our websites in-house. We don’t have any requirements as to what tools you use for your design, but we ask that you follow these guidelines.

IMAGES:
If you use any images or icons in the design, we ask that you have a link to the asset so we can purchase the image/icon. Most of the designs we submit do not have the customer’s images on them unless they have some great images. Be creative; show us the feeling you are trying to portray with your image choices. Use any royalty-free site you choose. We subscribe to Veltro and mainly use their images, but we can purchase images outside of Veltro. PLEASE NOTE: we will not submit designs to clients with watermarks on the images.

FONTS:
We ask that you identify the fonts you’re using in the design. This can be done in a message if you want. We typically use Plimsa Fonts and Veltro Fonts.

CONTENT:
We're always open to different content and ideas. We often submit designs with stock images so the client can see our vision. We typically take pictures after the website launch to use their images with our vision. Lorem Ipsum is fine for paragraphs, but we ask that you make the Headers with correct English. We want to be able to show the vision and identify the sections of the website.

INSPIRATION:
We typically add a couple of links in the brief of websites we like to help you get started in your design.

REVISIONS:
We do not often ask for revisions of the designs unless we see something in the design that may not appeal to the client. If there are slight changes that we want to make, we do that in the development process.

FEEDBACK:
We rarely give feedback on designs during the design process. We are working on many website projects and do not have the time to provide feedback. We usually respond if your request is well thought out and asks specific questions, but a note asking “feedback, please” usually goes unanswered.

```html
<!DOCTYPE html>
<html lang="en">
<head>
<meta charset="utf-8">
<title>Summit Haul – Trucking Company</title>
<link href="https://fonts.googleapis.com/css2?family=Poppins:wght@400;500;600;700&family=Bebas+Neue&display=swap" rel="stylesheet">
<style>
:root{
  --blue:#1479b8;
  --red:#f3344b;
  --red-dark:#b51d30;
  --ink:#333;
  --muted:#777;
  --light:#f0f0f0;
  --lighter:#f6f6f6;
  --white:#fff;
}
*{box-sizing:border-box;margin:0;padding:0}
html,body{width:1200px;height:4471px;overflow:hidden}
body{font-family:"Poppins",sans-serif;color:var(--ink);background:var(--white);position:relative}
.abs{position:absolute}
.photo{position:absolute}
/* header */
.site-header{position:absolute;top:0;left:0;width:1200px;height:171px;background:var(--white)}
.brand{position:absolute;display:flex;align-items:center;gap:10px;font-weight:700;color:var(--blue);letter-spacing:.5px}
.brand .mark{background:var(--red);display:inline-block}
.main-nav{position:absolute;top:72px;left:445px;display:flex;gap:0;font-size:15px}
.main-nav a{color:#444;text-decoration:none;position:absolute;white-space:nowrap}
.main-nav a.active{color:var(--red)}
.main-nav a.active::after{content:"";position:absolute;left:0;right:0;bottom:-12px;height:2px;background:var(--red)}
.btn{display:flex;align-items:center;justify-content:center;text-decoration:none;font-weight:500}
.quote-btn{position:absolute;left:962px;top:57px;width:148px;height:53px;background:var(--blue);color:#fff;font-size:15px;border-radius:2px}
/* hero */
.hero{position:absolute;top:171px;left:0;width:1200px;height:580px;overflow:hidden}
.hero-kicker{position:absolute;top:140px;left:650px;width:460px;text-align:center;color:#fff;font-weight:600;font-size:28px}
.hero-title{position:absolute;top:178px;left:650px;width:460px;text-align:center;color:#fff;font-family:"Bebas Neue",sans-serif;font-size:118px;line-height:1;letter-spacing:2px}
.hero-sub{position:absolute;top:302px;left:650px;width:460px;text-align:center;color:#fff;font-family:"Bebas Neue",sans-serif;font-size:60px;line-height:1}
.hero-btn{position:absolute;left:770px;top:400px;width:237px;height:79px;background:#222;color:#fff;font-size:20px;font-weight:600;border-radius:3px}
.dots{position:absolute;left:564px;top:528px;display:flex;gap:6px}
.dots span{width:13px;height:13px;border-radius:50%;background:#ddd}
.dots span:first-child{background:#fff}
/* headings */
.sec-head{position:absolute;text-align:right}
.sec-head h2{color:var(--blue);font-weight:700;font-size:38px;line-height:1.05}
.sec-head p{color:#555;font-size:27px;line-height:1.05;letter-spacing:.5px}
/* services */
.svc-card{position:absolute;top:1003px;width:245px;height:322px;background:#fff;border:1px solid #e2e2e2;box-shadow:0 2px 4px rgba(0,0,0,.08);text-align:center}
.svc-card .photo{left:6px;top:5px;width:233px;height:144px}
.svc-card h3{position:absolute;top:176px;width:100%;color:var(--blue);font-size:17px;font-weight:600}
.svc-card p{position:absolute;top:215px;left:16px;right:16px;font-size:12.5px;line-height:20px;color:var(--muted)}
.svc-card .more{position:absolute;left:102px;top:302px;width:40px;height:40px;background:#fff;border:1px solid #ddd;border-radius:3px;display:flex;align-items:center;justify-content:center}
.svc-card .more.on{border-color:var(--red)}
/* about */
.about{position:absolute;top:1433px;left:0;width:1200px;height:629px;background:var(--light);overflow:hidden}
.about-text{position:absolute;left:86px;top:228px;width:401px;font-size:15.5px;line-height:31px;color:#444;text-align:justify}
.read-more{position:absolute;left:86px;top:477px;width:143px;height:60px;background:var(--blue);color:#fff;font-size:15px}
/* why */
.reason{position:absolute;width:300px}
.reason h4{font-size:21px;font-weight:600;line-height:1.2}
.reason p{font-size:15px;line-height:19px;color:#444;margin-top:6px}
.reason.l{text-align:right}
.reason.red h4{color:var(--red)}
.reason.blue h4{color:var(--blue)}
.icon-dot{position:absolute;width:124px;height:124px;border-radius:50%;display:flex;align-items:center;justify-content:center;border:4px solid #fff;box-shadow:0 0 0 1px rgba(0,0,0,.03)}
.icon-dot.red{background:var(--red)}
.icon-dot.blue{background:var(--blue)}
/* testimonials */
.testi{position:absolute;top:2965px;left:0;width:1200px;height:638px;background:var(--lighter)}
.stars{position:absolute;top:288px;left:0;width:1200px;text-align:center;color:#f6b11a;font-size:24px;letter-spacing:2px}
.quote{position:absolute;top:328px;left:272px;width:656px;text-align:center;font-size:15px;line-height:26px;color:#444}
.author{position:absolute;top:500px;left:487px;display:flex;align-items:center;gap:10px}
.author .avatar{width:66px;height:66px;border-radius:50%}
.author b{display:block;font-size:15px;font-weight:600;color:#222}
.author span{font-size:13px;color:#555}
/* contact */
.contact-title{position:absolute;left:508px;top:3693px;color:var(--blue);font-size:30px;font-weight:700}
.field{position:absolute;border-bottom:1px solid #bbb;font-size:15px;color:#666;padding-bottom:18px}
.submit{position:absolute;left:508px;top:3937px;width:200px;height:60px;background:var(--red);color:#fff;font-size:15px;border-radius:6px}
/* footer */
.footer{position:absolute;top:4080px;left:0;width:1200px;height:332px;background:var(--light)}
.footer h5{position:absolute;top:80px;color:var(--blue);font-size:14px;font-weight:500;letter-spacing:.5px}
.links{position:absolute;left:373px;top:126px;list-style:none;font-size:15px;line-height:31px;color:#333}
.links li::before{content:"› ";color:var(--red);font-weight:700}
.contact-list{position:absolute;left:562px;top:127px;font-size:15px;color:#333}
.contact-list div{display:flex;gap:12px;margin-bottom:18px;line-height:17px}
.contact-list svg{flex:none}
.news-text{position:absolute;left:865px;top:124px;width:250px;font-size:15px;line-height:20px}
.news-input{position:absolute;left:865px;top:183px;width:248px;height:37px;background:#fff;border:1px solid #ddd;font-size:11px;color:#999;padding:11px 10px;letter-spacing:.5px}
.news-btn{position:absolute;left:865px;top:234px;width:126px;height:38px;background:var(--red);color:#fff;font-size:13px}
.copyright{position:absolute;top:4412px;left:0;width:1200px;height:59px;background:var(--blue);color:#fff;font-size:15px;display:flex;align-items:center;justify-content:center}
</style>
</head>
<body>

<header class="site-header">
  <div class="brand" style="left:87px;top:58px;font-size:34px"><span>SUMMIT HAUL</span><span class="mark" style="width:26px;height:26px"></span></div>
  <nav class="main-nav">
    <a class="active" style="left:0">Home</a>
    <a style="left:83px">Services</a>
    <a style="left:183px">About Us</a>
    <a style="left:290px">Testimonials</a>
    <a style="left:423px">Contact</a>
  </nav>
  <a class="btn quote-btn">Get a Quote</a>
</header>

<section class="hero">
  <div class="photo" role="img" aria-label="Red semi truck driving on a desert highway" style="left:0;top:0;width:800px;height:580px;background:linear-gradient(160deg,#e4e4e2 0%,#b9b3a6 40%,#8a6a45 70%,#4c4a48 100%)"></div>
  <svg class="abs" style="left:0;top:0" width="1200" height="580" viewBox="0 0 1200 580">
    <polygon points="410,0 1200,0 1200,580 790,580 600,310" fill="#f3344b"/>
    <polygon points="600,310 790,580 390,580" fill="#b51d30"/>
    <polygon points="600,310 790,580 700,580" fill="#d52a40"/>
  </svg>
  <div class="hero-kicker">SUMMIT HAUL</div>
  <div class="hero-title">THE BEST</div>
  <div class="hero-sub">TRUCKING COMPANY</div>
  <a class="btn hero-btn">GET A FREE QUOTE</a>
  <div class="dots"><span></span><span></span><span></span><span></span></div>
</section>

<div class="sec-head" style="left:380px;top:862px;width:310px">
  <h2>WHAT WE DO</h2><p>OUR SERVICES</p>
</div>

<article class="svc-card" style="left:85px">
  <div class="photo" role="img" aria-label="Cracked dry dirt" style="background:linear-gradient(135deg,#8b6a4a,#5e4630)"></div>
  <h3>DIRT</h3>
  <p>Lorem ipsum dolor sit amet, consectetur adipiscing elit, sed do eiusmod tempor incididunt</p>
  <span class="more"><svg width="14" height="18" viewBox="0 0 14 18"><path d="M2 1 L12 9 L2 17 L6 9Z" fill="#f3344b"/></svg></span>
</article>
<article class="svc-card" style="left:347px">
  <div class="photo" role="img" aria-label="Close-up of grey gravel" style="background:linear-gradient(135deg,#8f8880,#5d5853)"></div>
  <h3>GRAVEL</h3>
  <p>Lorem ipsum dolor sit amet, consectetur adipiscing elit, sed do eiusmod tempor incididunt</p>
  <span class="more on"><svg width="14" height="18" viewBox="0 0 14 18"><path d="M2 1 L12 9 L2 17 L6 9Z" fill="#f3344b"/></svg></span>
</article>
<article class="svc-card" style="left:609px">
  <div class="photo" role="img" aria-label="Bins of landscape bark and mulch" style="background:linear-gradient(90deg,#4f5b3c,#8c6a44,#6b4a2e,#3b3a34)"></div>
  <h3>LANDSCAPE BARK</h3>
  <p>Lorem ipsum dolor sit amet, consectetur adipiscing elit, sed do eiusmod tempor incididunt</p>
  <span class="more"><svg width="14" height="18" viewBox="0 0 14 18"><path d="M2 1 L12 9 L2 17 L6 9Z" fill="#f3344b"/></svg></span>
</article>
<article class="svc-card" style="left:870px">
  <div class="photo" role="img" aria-label="Stacked landscape stones" style="background:linear-gradient(135deg,#a0764a,#6b4c30)"></div>
  <h3>LANDSCAPE MATERIALS</h3>
  <p>Lorem ipsum dolor sit amet, consectetur adipiscing elit, sed do eiusmod tempor incididunt</p>
  <span class="more"><svg width="14" height="18" viewBox="0 0 14 18"><path d="M2 1 L12 9 L2 17 L6 9Z" fill="#f3344b"/></svg></span>
</article>

<section class="about">
  <svg class="abs" style="left:0;top:0" width="1200" height="629">
    <rect x="860" y="0" width="340" height="629" fill="#f3344b"/>
    <circle cx="860" cy="317" r="322" fill="#fff"/>
    <circle cx="860" cy="317" r="295" fill="#1479b8"/>
  </svg>
  <div class="photo" role="img" aria-label="White semi trucks driving on a road through pine forest" style="left:595px;top:52px;width:530px;height:530px;border-radius:50%;background:linear-gradient(160deg,#bcd3e4 0%,#6f8a4e 45%,#e9ecee 70%,#5a5f62 100%)"></div>
  <div class="sec-head" style="left:90px;top:108px;width:270px">
    <h2>WHO WE ARE</h2><p>OUR COMPANY</p>
  </div>
  <p class="about-text">Lorem ipsum dolor sit amet, consectetur adipiscing elit, sed do eiusmod tempor incididunt ut labore et dolore magna aliqua. Ut enim ad minim veniam, quis nostrud exercitation ullamco laboris nisi ut aliquip ex ea commodo consequat. Duis aute irure dolor in reprehenderit in voluptate velit esse cillum dolore eu fugiat nulla pariatur.</p>
  <a class="btn read-more">Read More</a>
</section>

<div class="sec-head" style="left:380px;top:2185px;width:345px">
  <h2>WHY CHOOSE US</h2><p style="font-size:24px">6 REASONS WHY TO CHOOSE<br>OUR TRUCKING COMPANY</p>
</div>

<svg class="abs" style="left:380px;top:2405px" width="440" height="440">
  <circle cx="220" cy="220" r="215" fill="none" stroke="#f3344b" stroke-width="3"/>
</svg>
<div class="photo" role="img" aria-label="Red semi truck on a highway" style="left:435px;top:2460px;width:330px;height:330px;border-radius:50%;background:linear-gradient(160deg,#e6e6e4,#a8957a 55%,#55504a)"></div>

<div class="icon-dot red" style="left:413px;top:2368px"><svg width="60" height="44" viewBox="0 0 60 44"><rect x="4" y="8" width="30" height="22" fill="#fff"/><path d="M34 14h12l8 10v6H34z" fill="#fff"/><circle cx="14" cy="34" r="6" fill="#fff" stroke="#f3344b" stroke-width="3"/><circle cx="44" cy="34" r="6" fill="#fff" stroke="#f3344b" stroke-width="3"/></svg></div>
<div class="icon-dot blue" style="left:663px;top:2368px"><svg width="60" height="40" viewBox="0 0 60 40"><path d="M6 8h34l12 12v10H6z" fill="#fff"/><circle cx="16" cy="32" r="5" fill="#1479b8" stroke="#fff" stroke-width="3"/><circle cx="42" cy="32" r="5" fill="#1479b8" stroke="#fff" stroke-width="3"/></svg></div>
<div class="icon-dot blue" style="left:311px;top:2553px"><span style="color:#fff;font-size:56px;font-weight:600">$</span></div>
<div class="icon-dot red" style="left:748px;top:2553px"><svg width="60" height="44" viewBox="0 0 60 44"><circle cx="14" cy="14" r="11" fill="none" stroke="#fff" stroke-width="3"/><path d="M14 8v6h5" stroke="#fff" stroke-width="3" fill="none"/><path d="M24 16h18l10 10v8H24z" fill="#fff"/><circle cx="32" cy="36" r="5" fill="#fff" stroke="#f3344b" stroke-width="3"/></svg></div>
<div class="icon-dot red" style="left:413px;top:2738px"><svg width="44" height="50" viewBox="0 0 44 50"><circle cx="22" cy="13" r="11" fill="#fff"/><path d="M2 50c0-14 8-22 20-22s20 8 20 22z" fill="#fff"/><path d="M20 28l2 14 2-14z" fill="#f3344b"/></svg></div>
<div class="icon-dot blue" style="left:663px;top:2738px"><svg width="50" height="44" viewBox="0 0 50 44"><rect x="4" y="24" width="8" height="18" fill="#fff"/><rect x="16" y="18" width="8" height="24" fill="#fff"/><rect x="28" y="22" width="8" height="20" fill="#fff"/><rect x="40" y="12" width="8" height="30" fill="#fff"/><path d="M4 16l12-8 12 6 18-12" stroke="#fff" stroke-width="3" fill="none"/></svg></div>

<div class="reason l red" style="left:77px;top:2390px"><h4>On-Time Delivery</h4><p>Lorem ipsum dolor tempor<br>amet, consectetur adipiscing elit</p></div>
<div class="reason blue" style="left:810px;top:2382px"><h4>Real-Time Tracking</h4><p>Lorem ipsum dolor tempor<br>amet, consectetur adipiscing elit</p></div>
<div class="reason l blue" style="left:-7px;top:2578px"><h4>Cost Optimization</h4><p>Lorem ipsum dolor tempor<br>amet, consectetur adipiscing</p></div>
<div class="reason red" style="left:890px;top:2567px"><h4>Reduced Transit Time</h4><p>Lorem ipsum dolor tempor<br>amet, consectetur adipiscing elit<br>Lorem ipsum dolor</p></div>
<div class="reason l red" style="left:85px;top:2780px"><h4>Experienced Staff</h4><p>Lorem ipsum dolor tempor<br>amet, consectetur adipiscing<br>elitLorem ipsum dolor</p></div>
<div class="reason blue" style="left:810px;top:2770px"><h4>24/7 Online Support</h4><p>Lorem ipsum dolor tempor<br>amet, consectetur adipiscing elit</p></div>

<section class="testi">
  <div class="sec-head" style="left:270px;top:120px;width:560px">
    <h2>OUR SATISFIED CUSTOMERS</h2><p>TESTIMONIALS</p>
  </div>
  <div class="stars">★★★★★</div>
  <p class="quote">Lorem ipsum dolor sit amet, consectetur adipiscing elit. Integer vulputate nunc nec ligula viverra ultrices. Phasellus scelerisque luctus mi non venenatis. Morbi sapien enim, egestas et augue ac, aliquam mattis libero. Vestibulum non lacus vel eros suscipit commodo. Vestibulum non lectus faucibus, laoreet nisl id, faucibus turpis. Fusce eu neque nec libero semper efficitur non vel tellus</p>
  <svg class="abs" style="left:164px;top:367px" width="24" height="36"><path d="M20 2L4 18l16 16" stroke="#999" stroke-width="4" fill="none"/></svg>
  <svg class="abs" style="left:1014px;top:367px" width="24" height="36"><path d="M4 2l16 16L4 34" stroke="#999" stroke-width="4" fill="none"/></svg>
  <div class="author">
    <div class="avatar" role="img" aria-label="Customer portrait" style="background:linear-gradient(160deg,#c9d6e2,#5d6f82)"></div>
    <div><b>Lorem ipsum dolor</b><span>Ipsum dolor lorem</span></div>
  </div>
</section>

<svg class="abs" style="left:90px;top:3650px" width="370" height="360">
  <path d="M180 6 A170 170 0 0 1 180 346" transform="translate(10,0)" fill="none" stroke="#f3344b" stroke-width="10"/>
</svg>
<div class="photo" role="img" aria-label="Red semi truck parked on a country road" style="left:100px;top:3655px;width:340px;height:340px;border-radius:50%;background:linear-gradient(160deg,#d8dde0,#9aa3a6 45%,#b23a3a 60%,#6a6058)"></div>
<h2 class="contact-title">HOW CAN WE HELP YOU?</h2>
<div class="field" style="left:508px;top:3800px;width:255px">Name</div>
<div class="field" style="left:816px;top:3800px;width:255px">E-Mail</div>
<div class="field" style="left:508px;top:3867px;width:560px">Message</div>
<a class="btn submit">SUBMIT NOW</a>

<footer class="footer">
  <div class="brand" style="left:90px;top:160px;font-size:33px"><span>SUMMIT HAUL</span><span class="mark" style="width:24px;height:24px"></span></div>
  <h5 style="left:373px">QUICK LINKS</h5>
  <ul class="links"><li>Home</li><li>Services</li><li>About Us</li><li>Testimonials</li><li>Contact</li></ul>
  <h5 style="left:562px">CONTACT US</h5>
  <div class="contact-list">
    <div><svg width="20" height="20" viewBox="0 0 20 20"><rect x="1" y="1" width="18" height="18" rx="2" fill="none" stroke="#f3344b"/><path d="M6 5c0 6 3 9 9 10l1-3-3-1-1 1c-2-1-3-2-4-4l1-1-1-3z" fill="#f3344b"/></svg>+012 555 0184</div>
    <div><svg width="20" height="20" viewBox="0 0 20 20"><rect x="1" y="1" width="18" height="18" rx="2" fill="none" stroke="#f3344b"/><rect x="5" y="6" width="10" height="8" fill="#f3344b"/><path d="M5 6l5 4 5-4" stroke="#fff" fill="none"/></svg>hello@summithaul.example</div>
    <div><svg width="20" height="20" viewBox="0 0 20 20"><rect x="1" y="1" width="18" height="18" rx="2" fill="none" stroke="#f3344b"/><path d="M10 4a4 4 0 0 1 4 4c0 3-4 8-4 8s-4-5-4-8a4 4 0 0 1 4-4z" fill="#f3344b"/><circle cx="10" cy="8" r="1.5" fill="#fff"/></svg><span>Address line Dummy Here<br>Address line Here</span></div>
  </div>
  <h5 style="left:865px">OUR NEWSLETTER</h5>
  <p class="news-text">Subscribe our newsletter to get the latest news.</p>
  <div class="news-input">ENTER YOUR EMAIL</div>
  <a class="btn news-btn">SUBSCRIBE</a>
</footer>
<div class="copyright">Copyright © 2023 All Rights Reserved By Summit Haul</div>

</body>
</html>
```